Business Card Design needed for logo design project

Our business needs a business card design. I'm not sure what format files are generally delivered back, but clearly I will need the ability to edit to add colleagues contact details.

Our logo is attached.

Brivanor is a 3D design services company, providing app, serious/educational game, VR and AR websites/applications to corporate clients.

Target Market(s)

Corporate blue-chip clients needing 3D design services

Industry/Entity Type

Business

Font styles to use
Sans Serif

Requirements
Must have
• Templated such that I can add details (name, phone number etc). Needs to include logo from previous project winner - attached.

```html
<!DOCTYPE html>
<html lang="en">
<head>
<meta charset="utf-8">
<title>Brivanor Business Card</title>
<link rel="stylesheet" href="https://fonts.googleapis.com/css2?family=Montserrat:wght@300;400;600;700&display=swap">
<style>
  :root {
    --bg: #2a2a2c;
    --card-dark: #111113;
    --card-mid: #232326;
    --red: #e41e2b;
    --white: #ffffff;
    --grey-text: #d6d6d8;
    --faint: rgba(255,255,255,0.035);
  }
  * { box-sizing: border-box; margin: 0; padding: 0; }
  html, body { width: 1200px; height: 900px; overflow: hidden; }
  body {
    background: var(--bg);
    font-family: "Montserrat", Arial, sans-serif;
    position: relative;
  }
  .card {
    position: absolute;
    left: 320px;
    width: 560px;
    height: 320px;
    border-radius: 18px;
    overflow: hidden;
    background: linear-gradient(135deg, var(--card-mid) 0%, var(--card-dark) 70%);
    box-shadow: 0 14px 30px rgba(0,0,0,0.45);
  }
  .card--back { top: 100px; }
  .card--front { top: 480px; }

  /* back */
  .back-decor { position: absolute; left: -60px; top: -20px; }
  .services {
    position: absolute;
    left: 300px; top: 44px;
    list-style: none;
    color: var(--grey-text);
    font-size: 13px;
    font-weight: 400;
    line-height: 20px;
  }
  .services li::before {
    content: "";
    display: inline-block;
    width: 5px; height: 5px;
    border-radius: 50%;
    background: var(--red);
    margin-right: 8px;
    vertical-align: middle;
  }
  .back-brand {
    position: absolute;
    left: 150px; bottom: 42px;
    display: flex; align-items: center; gap: 14px;
  }
  .brand-dot { width: 46px; height: 46px; border-radius: 50%; background: var(--red); flex: none; }
  .back-brand .wordmark { color: var(--red); font-size: 44px; }
  .wordmark { font-weight: 300; letter-spacing: 3px; line-height: 1; white-space: nowrap; }

  /* front */
  .front-disc { position: absolute; left: 0; top: 0; }
  .contact { position: absolute; left: 280px; top: 42px; color: var(--white); }
  .contact-name { font-size: 22px; font-weight: 700; letter-spacing: 0.5px; }
  .contact-title { color: var(--red); font-size: 12px; margin-top: 2px; margin-bottom: 10px; }
  .contact-list { list-style: none; font-size: 12px; color: var(--grey-text); }
  .contact-list li { display: flex; align-items: center; gap: 8px; height: 20px; }
  .contact-list .icon { width: 14px; height: 14px; flex: none; }
  .contact-web { margin-top: 10px; font-weight: 700; color: var(--white); font-size: 13px; }
  .front-wordmark {
    position: absolute;
    left: 282px; bottom: 46px;
    color: var(--white);
    font-size: 40px;
    letter-spacing: 2px;
  }
</style>
</head>
<body>

<section class="card card--back" aria-label="Card back">
  <svg class="back-decor" width="320" height="320" viewBox="0 0 320 320" aria-hidden="true">
    <circle cx="160" cy="160" r="150" fill="var(--faint)"/>
  </svg>
  <ul class="services">
    <li>3D design services</li>
    <li>Application</li>
    <li>Serious/educational game</li>
    <li>VR and AR</li>
    <li>Websites/applications</li>
  </ul>
  <div class="back-brand">
    <span class="brand-dot"></span>
    <span class="wordmark">BRIVANOR</span>
  </div>
</section>

<section class="card card--front" aria-label="Card front">
  <svg class="front-disc" width="270" height="320" viewBox="0 0 270 320" aria-hidden="true">
    <circle cx="100" cy="170" r="170" fill="var(--red)"/>
  </svg>
  <div class="contact">
    <p class="contact-name">DEAN HOLLIS</p>
    <p class="contact-title">Your title here</p>
    <ul class="contact-list">
      <li>
        <svg class="icon" viewBox="0 0 14 14" aria-hidden="true"><circle cx="7" cy="7" r="7" fill="var(--red)"/><path d="M4.5 3.5l1.5 0 .7 1.8-.9.7a5 5 0 0 0 2.2 2.2l.7-.9 1.8.7v1.5c-3.5 0-6-2.5-6-6z" fill="var(--white)"/></svg>
        +61 XXX XXX XXX
      </li>
      <li>
        <svg class="icon" viewBox="0 0 14 14" aria-hidden="true"><circle cx="7" cy="7" r="7" fill="var(--red)"/><rect x="3.5" y="4.5" width="7" height="5" fill="none" stroke="var(--white)" stroke-width="1"/><path d="M3.5 4.5L7 7.2l3.5-2.7" fill="none" stroke="var(--white)" stroke-width="1"/></svg>
        dean@brivanor.com.au
      </li>
      <li>
        <svg class="icon" viewBox="0 0 14 14" aria-hidden="true"><circle cx="7" cy="7" r="7" fill="var(--red)"/></svg>
        @brivanor
      </li>
      <li class="contact-web">
        <svg class="icon" viewBox="0 0 14 14" aria-hidden="true"><circle cx="7" cy="7" r="7" fill="var(--red)"/><circle cx="7" cy="7" r="3.5" fill="none" stroke="var(--white)" stroke-width="1"/></svg>
        www.brivanor.com.au
      </li>
    </ul>
  </div>
  <span class="wordmark front-wordmark">BRIVANOR</span>
</section>

</body>
</html>
```